Borealis Pictures are looking for a poster design for a new short film called "Paper Lanterns"
The film will be submitted to all major film festivals so great exposure....

Paper Lanterns was written and directed by Leo Brantley. Produced by Borealis Pictures. Starring Ray Cobden, Hannah Pryce, Tom Brantley, Neil Fairbrook and Gavin Ross.

Synopsis: Paper Lanterns, tells the story of Vic. A want-away agent/hit man for an undisclosed body, who is sent on a mysterious mission for his final assignment.
Whilst waiting on his last instructions in a hideaway, he meets Olena and Hugh and begins to snatch at the real life he's craved for so long.
In danger of taking his eye off the ball too soon, Vic must kill time and fight loneliness, for just one more day.

To give you an feel for the film here is the trailer on Youtube http://www.clipvault-example.com/watch?v=qL7mZt2PxRa.

Please can you put borealis website www.borealispictures-example.co.uk on the design.

Best of luck

```html
<!DOCTYPE html>
<html lang="en">
<head>
<meta charset="utf-8">
<title>Paper Lanterns — Borealis Pictures</title>
<link rel="stylesheet" href="https://fonts.googleapis.com/css2?family=Amatic+SC:wght@400;700&display=swap">
<style>
  :root {
    --ink-black: #0b0b0b;
    --blood-red: #d42a22;
    --deep-red: #7e0c0c;
    --mid-red: #b31414;
    --chalk-white: #f1efec;
  }
  html, body {
    margin: 0;
    padding: 0;
    width: 792px;
    height: 1200px;
    overflow: hidden;
    background: var(--ink-black);
  }
  .poster {
    position: relative;
    width: 792px;
    height: 1200px;
    background: var(--ink-black);
    font-family: "Amatic SC", "Comic Sans MS", cursive;
    color: var(--chalk-white);
    text-align: center;
    text-transform: uppercase;
    overflow: hidden;
  }
  .key-art {
    position: absolute;
    left: 0;
    top: 0;
    width: 792px;
    height: 790px;
    background:
      radial-gradient(ellipse 190px 300px at 215px 420px, var(--mid-red) 0%, var(--deep-red) 55%, rgba(126, 12, 12, 0) 100%),
      radial-gradient(ellipse 130px 190px at 600px 590px, var(--mid-red) 0%, var(--deep-red) 55%, rgba(126, 12, 12, 0) 100%),
      radial-gradient(ellipse 140px 210px at 480px 250px, var(--mid-red) 0%, var(--deep-red) 55%, rgba(126, 12, 12, 0) 100%),
      radial-gradient(ellipse 80px 150px at 650px 300px, var(--deep-red) 0%, rgba(126, 12, 12, 0) 100%),
      radial-gradient(ellipse 120px 50px at 320px 700px, var(--deep-red) 0%, rgba(126, 12, 12, 0) 100%);
  }
  .credits-line {
    position: absolute;
    left: 0;
    width: 100%;
    margin: 0;
    font-size: 30px;
    font-weight: 400;
    letter-spacing: 3px;
    line-height: 1;
    white-space: nowrap;
  }
  .accent { color: var(--blood-red); }
  .light { color: var(--chalk-white); }
  .credit-director { top: 806px; }
  .credit-producer { top: 854px; }
  .film-title {
    position: absolute;
    left: 0;
    width: 100%;
    top: 892px;
    margin: 0;
    font-size: 128px;
    font-weight: 400;
    letter-spacing: 4px;
    line-height: 1;
    white-space: nowrap;
  }
  .credit-cast-lead { top: 1042px; }
  .credit-cast-support { top: 1090px; }
  .website {
    position: absolute;
    left: 0;
    width: 100%;
    top: 1144px;
    margin: 0;
    font-size: 20px;
    font-weight: 400;
    letter-spacing: 4px;
    line-height: 1;
    white-space: nowrap;
  }
</style>
</head>
<body>
  <main class="poster">
    <div class="key-art" role="img" aria-label="Red-toned illustration of the film's characters: a man in profile, a raised knife, a woman's face and a small figure on a bench"></div>

    <p class="credits-line credit-director"><span class="accent">Written and directed by</span> <span class="light">Leo Brantley</span></p>
    <p class="credits-line credit-producer"><span class="light">Produced by</span> <span class="accent">Borealis Pictures</span></p>

    <h1 class="film-title"><span class="light">Paper</span> <span class="accent">Lanterns</span></h1>

    <p class="credits-line credit-cast-lead"><span class="accent">Starring</span> <span class="light">Ray Cobden</span> <span class="accent">Hannah Pryce</span></p>
    <p class="credits-line credit-cast-support"><span class="light">Tom Brantley</span> <span class="accent">Neil Fairbrook</span> <span class="light">Gavin Ross</span></p>

    <p class="website"><span class="accent">www.borealispictures-example</span><span class="light">.co.uk</span></p>
  </main>
</body>
</html>
```